Quimby's Yard & Garden Center Business Card Update

I need an updated Business card design for my Lawn and Garden Center. We do Landscaping installs, Lawn Mowing, Snow Removal and also have a Garden Center Retail Division. I uploaded a few of our previous business cards to give an idea of what we are starting with. The main goal of this update is to simplify and modernize the business card, not all of the services that are on the previous cards has to be on the new one but I would still like to highlight our main services. There is also a sample of our logo that Can be used in the design.

Industry/Entity Type

Landscaping

Contact Information for Business Card

Morris Quimby
Morris@Quimbysyardandgarden.example
Business (555) 201-7784
Cell (555) 318-6092

Colors

Designer to choose colors to be used in the design.

Requirements
Must have
• Services Provided :
• Landscaping
• Lawn Maintenance
• Snow Removal
• Garden Center

```html
<!DOCTYPE html>
<html lang="en">
<head>
<meta charset="utf-8">
<title>Quimby's Yard &amp; Garden Center — Business Card</title>
<link rel="stylesheet" href="https://fonts.googleapis.com/css2?family=Lato:wght@400;700&family=Open+Sans:wght@400&display=swap">
<style>
  :root {
    --card-bg: #ffffff;
    --card-edge: #c9c9c9;
    --ink: #333333;
    --ink-soft: #3a3a3a;
    --forest: #2c5527;
    --leaf: #3f8a2e;
    --lime-top: #aac829;
    --lime-bottom: #6e9a2f;
    --tagline-lime: #8db53c;
    --white: #ffffff;
  }
  html, body {
    margin: 0;
    padding: 0;
    width: 1200px;
    height: 757px;
    overflow: hidden;
    background: var(--card-bg);
  }
  .card {
    position: relative;
    width: 1200px;
    height: 757px;
    box-sizing: border-box;
    border: 2px solid var(--card-edge);
    background: var(--card-bg);
    overflow: hidden;
    font-family: "Open Sans", Arial, sans-serif;
  }
  .accent-band {
    position: absolute;
    inset: 0;
    width: 100%;
    height: 100%;
  }
  .services {
    position: absolute;
    left: 106px;
    top: 92px;
  }
  .services__title {
    margin: 0;
    font-family: "Lato", Arial, sans-serif;
    font-weight: 400;
    font-size: 25px;
    letter-spacing: 0.5px;
    color: var(--ink-soft);
    padding-bottom: 6px;
    width: 258px;
    border-bottom: 2px solid var(--ink-soft);
    position: relative;
  }
  .services__title::after {
    content: "";
    position: absolute;
    left: 0;
    bottom: -3px;
    width: 48px;
    height: 4px;
    background: var(--leaf);
  }
  .services__list {
    list-style: none;
    margin: 22px 0 0 0;
    padding: 0;
  }
  .services__item {
    position: relative;
    font-family: "Lato", Arial, sans-serif;
    font-weight: 700;
    font-size: 26px;
    line-height: 38px;
    color: var(--ink-soft);
  }
  .services__item::before {
    content: "";
    position: absolute;
    left: -22px;
    top: 15px;
    width: 7px;
    height: 7px;
    background: var(--forest);
    transform: rotate(45deg);
  }
  .brand {
    position: absolute;
    left: 730px;
    top: 150px;
    width: 380px;
    display: flex;
    align-items: center;
    justify-content: center;
    gap: 18px;
  }
  .brand__dot {
    width: 26px;
    height: 26px;
    border-radius: 50%;
    background: var(--forest);
  }
  .brand__name {
    font-family: "Open Sans", Arial, sans-serif;
    font-weight: 400;
    font-size: 76px;
    color: var(--forest);
    line-height: 1;
  }
  .contact {
    position: absolute;
    left: 72px;
    top: 526px;
    margin: 0;
    font-style: normal;
    font-size: 24px;
    line-height: 37.5px;
    color: var(--ink);
  }
  .contact p { margin: 0; }
  .tagline {
    position: absolute;
    left: 900px;
    top: 562px;
    font-family: "Open Sans", Arial, sans-serif;
    font-size: 35px;
    line-height: 42px;
  }
  .tagline__lead {
    display: block;
    color: var(--tagline-lime);
    padding-left: 84px;
  }
  .tagline__main {
    display: block;
    color: var(--white);
  }
</style>
</head>
<body>
  <div class="card">
    <svg class="accent-band" viewBox="0 0 1200 757" aria-hidden="true">
      <defs>
        <linearGradient id="lime-fade" x1="0" y1="0" x2="0" y2="1">
          <stop offset="0" stop-color="var(--lime-top)"/>
          <stop offset="1" stop-color="var(--lime-bottom)"/>
        </linearGradient>
      </defs>
      <polygon class="accent-band__field" points="660,420 1200,420 1200,757 880,757" fill="var(--forest)"/>
      <polygon class="accent-band__lime" points="575,420 632,420 852,757 795,757" fill="url(#lime-fade)"/>
    </svg>

    <section class="services">
      <h2 class="services__title">SERVICES PROVIDED</h2>
      <ul class="services__list">
        <li class="services__item">Landscaping</li>
        <li class="services__item">Lawn Maintenance</li>
        <li class="services__item">Snow Removal</li>
        <li class="services__item">Garden Center</li>
      </ul>
    </section>

    <div class="brand">
      <span class="brand__dot"></span>
      <span class="brand__name">Quimby's</span>
    </div>

    <address class="contact">
      <p>Morris Quimby</p>
      <p>Morris@Quimbysyardandgarden.example</p>
      <p>Business (555) 201-7784</p>
      <p>Cell (555) 318-6092</p>
    </address>

    <div class="tagline">
      <span class="tagline__lead">Where</span>
      <span class="tagline__main">Color Lives....</span>
    </div>
  </div>
</body>
</html>
```